Business Card for a mobile physiotherapy company

I need a layout for a business card for a mobile physiotherapy company.
Slogan is "Mobile Physiotherapy - Your Road To Recovery"
Phone number is 867-412-5093
Email VantePhysio@mailbox-demo.ca (subject to change with website)
Website www.VantePhysio.ca
My name and credentials: Gil Varney Gil Varney, BSc(kin), MPT, CAFCI, IMS
Information maybe included: Direct Billing, Services including Physiotherapy, IMS, acupuncture
Maybe include facebook and instagram logos
One side with the logo clean and sharp
Other side with details, try not to look too busy, keep everything concise

```html
<!DOCTYPE html>
<html lang="en">
<head>
<meta charset="utf-8">
<title>Vante Physio – Business Card</title>
<link rel="stylesheet" href="https://fonts.googleapis.com/css2?family=Roboto:ital,wght@0,400;0,500;0,700;1,400&display=swap">
<style>
  :root {
    --forest: #0b5449;
    --navy: #2c4a72;
    --navy-soft: #4a6791;
    --white: #ffffff;
    --paper: #ffffff;
    --ink-grey: #555b60;
    --backdrop: #e9e6e1;
  }
  * { box-sizing: border-box; margin: 0; padding: 0; }
  html, body {
    width: 1125px; height: 1200px; overflow: hidden;
    background: var(--backdrop);
    font-family: "Roboto", Arial, sans-serif;
  }
  .canvas { position: relative; width: 1125px; height: 1200px; }
  .card {
    position: absolute; left: 171px; width: 826px; height: 470px;
    overflow: hidden;
    box-shadow: 0 3px 8px rgba(0,0,0,0.25);
  }
  .card--front { top: 106px; background: var(--forest); color: var(--white); }
  .card--back { top: 639px; background: var(--paper); }

  .identity { position: absolute; left: 51px; top: 46px; }
  .identity__name { font-size: 29px; font-weight: 700; letter-spacing: 0.5px; line-height: 1; text-transform: uppercase; }
  .identity__creds { font-size: 19px; font-weight: 500; margin-top: 3px; }
  .identity__note { font-size: 19px; font-weight: 500; margin-top: 5px; }

  .contact { position: absolute; right: 46px; top: 50px; list-style: none; text-align: right; }
  .contact__item { font-size: 18.5px; line-height: 26px; display: flex; justify-content: flex-end; align-items: center; gap: 9px; }
  .contact__icon { width: 17px; height: 17px; fill: var(--white); flex: none; }

  .hero-art { position: absolute; left: 0; bottom: 0; width: 826px; height: 390px; }

  .social { position: absolute; right: 50px; top: 40px; display: flex; align-items: center; gap: 8px; color: var(--navy); font-size: 16px; font-weight: 500; }
  .social__dot { width: 20px; height: 20px; border-radius: 50%; background: var(--navy); }

  .brand {
    position: absolute; left: 0; right: 0; top: 215px; text-align: center;
    font-size: 56px; font-weight: 700; letter-spacing: 8px; color: var(--forest);
    text-transform: uppercase; line-height: 1;
  }
  .tagline { position: absolute; left: 0; right: 0; top: 380px; text-align: center; font-size: 19.5px; font-style: italic; color: var(--ink-grey); }
  .services { position: absolute; left: 0; right: 0; top: 408px; text-align: center; font-size: 19.5px; color: var(--forest); }
  .services__sep { font-size: 12px; vertical-align: middle; margin: 0 3px; }
</style>
</head>
<body>
<main class="canvas">

  <section class="card card--front">
    <div class="identity">
      <h1 class="identity__name">Gil Varney</h1>
      <p class="identity__creds">BSc(kin), MPT, CAFCI, IMS</p>
      <p class="identity__note">Direct Billing</p>
    </div>

    <ul class="contact">
      <li class="contact__item">867-412-5093
        <svg class="contact__icon" viewBox="0 0 24 24"><path d="M6.6 10.8a15.1 15.1 0 0 0 6.6 6.6l2.2-2.2a1 1 0 0 1 1-.25 11.4 11.4 0 0 0 3.6.57 1 1 0 0 1 1 1V20a1 1 0 0 1-1 1A17 17 0 0 1 3 4a1 1 0 0 1 1-1h3.5a1 1 0 0 1 1 1c0 1.25.2 2.45.57 3.57a1 1 0 0 1-.25 1z"/></svg>
      </li>
      <li class="contact__item">VantePhysio@mailbox-demo.ca
        <svg class="contact__icon" viewBox="0 0 24 24"><path d="M2 5h20v14H2z M3.5 6.5 12 13l8.5-6.5" fill="var(--white)" stroke="var(--forest)" stroke-width="1.4"/></svg>
      </li>
      <li class="contact__item">www.VantePhysio.ca
        <svg class="contact__icon" viewBox="0 0 24 24"><circle cx="12" cy="12" r="10"/><path d="M12 2v20M2 12h20M5 6.5c4 2 10 2 14 0M5 17.5c4-2 10-2 14 0" fill="none" stroke="var(--forest)" stroke-width="1.3"/></svg>
      </li>
    </ul>

    <svg class="hero-art" viewBox="0 0 826 390" role="img" aria-label="Illustration of mountain peaks above a house roof with a window">
      <defs>
        <linearGradient id="peakTone" x1="0" y1="0" x2="0" y2="1">
          <stop offset="0" stop-color="var(--navy)"/>
          <stop offset="1" stop-color="var(--navy-soft)"/>
        </linearGradient>
      </defs>
      <polygon points="0,390 420,0 826,390" fill="url(#peakTone)"/>
    </svg>
  </section>

  <section class="card card--back">
    <div class="social"><span class="social__dot"></span>@vantephysio</div>
    <p class="brand">Vante Physio</p>
    <p class="tagline">Mobile Physiotherapy - Your Road To Recovery</p>
    <p class="services">Physiotherapy<span class="services__sep">&#9679;</span>IMS<span class="services__sep">&#9679;</span>Acupuncture</p>
  </section>

</main>
</body>
</html>
```